Engineering Consultant Business Card

I'm starting a new business as a high-end engineering consultant in a niche field. I've attached the jpg for my logo plus the branding guideline document that I've been following. You can see my business website here: www.tarvikworks.com
I'd like a business card that has the logo on one side, then the other side has (in any order): Tarvik Works, Inc.
Dana Whitlock
President and Chief EMC Engineer
www.tarvikworks.com
dana@tarvikworks.com
Optional: motto "We will solve your EMC problems as early as possible—ideally before they even start."
I'm not planning on including a phone number
Target Market(s)
Businesses, especially makers of electronics hardware
Industry/Entity Type
Electrical engineering
Contact Information for Business Card
Company name, my name, website, email

```html
<!DOCTYPE html>
<html lang="en">
<head>
<meta charset="utf-8">
<title>Tarvik Works, Inc. — Business Card</title>
<link href="https://fonts.googleapis.com/css2?family=Poppins:wght@400;600;700&family=Oswald:wght@300&display=swap" rel="stylesheet">
<style>
  :root {
    --brand-blue: #2b45a3;
    --brand-blue-deep: #1f3588;
    --brand-blue-light: #3a56c4;
    --paper: #ffffff;
    --backdrop: #1c1c1c;
  }
  * { box-sizing: border-box; margin: 0; padding: 0; }
  html, body { width: 1200px; height: 1015px; overflow: hidden; }
  body {
    background: var(--backdrop);
    position: relative;
    font-family: "Poppins", sans-serif;
  }
  .card {
    position: absolute;
    width: 600px;
    height: 343px;
    overflow: hidden;
    box-shadow: 0 10px 30px rgba(0,0,0,.55);
  }
  .card--back { left: 120px; top: 90px; }
  .card--front { left: 480px; top: 560px; background: var(--paper); }

  .back-pattern {
    position: absolute; inset: 0;
    background: linear-gradient(135deg, var(--brand-blue-deep), var(--brand-blue) 50%, var(--brand-blue-light));
  }
  .back-mark {
    position: absolute; left: 50%; top: 50%;
    transform: translate(-50%, -50%);
    display: flex; align-items: center; gap: 8px;
    color: var(--paper);
    font-weight: 600; font-size: 15px;
  }
  .back-mark .dot {
    width: 16px; height: 16px; border: 2px solid var(--paper); border-radius: 50%;
  }

  .front-shape { position: absolute; inset: 0; }
  .contact {
    position: absolute; left: 44px; top: 62px;
    color: var(--paper);
  }
  .contact__name {
    font-weight: 700; font-size: 25px; letter-spacing: .5px; line-height: 1.1;
    text-transform: uppercase;
  }
  .contact__title { font-size: 16px; font-weight: 400; margin-top: 2px; }
  .contact__rule { width: 70px; height: 1px; background: var(--paper); margin: 16px 0; opacity: .85; }
  .contact__line { display: flex; align-items: center; gap: 8px; font-size: 17px; line-height: 1.35; }
  .contact__line svg { width: 15px; height: 15px; flex: none; }
  .contact__motto {
    font-family: "Oswald", sans-serif; font-weight: 300;
    font-size: 17px; line-height: 1.25; width: 250px;
  }
  .front-mark {
    position: absolute; left: 400px; top: 150px;
    display: flex; align-items: center; gap: 10px;
    color: var(--brand-blue);
    font-weight: 600; font-size: 19px; line-height: 1.15;
  }
  .front-mark .dot {
    width: 22px; height: 22px; border: 3px solid var(--brand-blue); border-radius: 50%; flex: none;
  }
</style>
</head>
<body>

<section class="card card--back">
  <div class="back-pattern" role="img" aria-label="Repeating embossed brand mark pattern in blue"></div>
  <div class="back-mark"><span class="dot"></span>Tarvik Works</div>
</section>

<section class="card card--front">
  <svg class="front-shape" viewBox="0 0 600 343" width="600" height="343" aria-hidden="true">
    <path d="M0 0 H300 Q420 170 300 343 H0 Z" fill="var(--brand-blue)"/>
    <path d="M314 0 Q432 170 314 343" fill="none" stroke="var(--brand-blue)" stroke-width="3"/>
  </svg>

  <div class="contact">
    <p class="contact__name">Dana Whitlock</p>
    <p class="contact__title">President and Chief EMC Engineer</p>
    <div class="contact__rule"></div>
    <p class="contact__line">
      <svg viewBox="0 0 16 16" fill="none" stroke="#fff" stroke-width="1.4"><circle cx="8" cy="8" r="6.5"/><ellipse cx="8" cy="8" rx="3" ry="6.5"/><path d="M1.5 8h13M3 4.5h10M3 11.5h10"/></svg>
      www.tarvikworks.com
    </p>
    <p class="contact__line">
      <svg viewBox="0 0 16 16" fill="none" stroke="#fff" stroke-width="1.4"><rect x="1.5" y="3.5" width="13" height="9"/><path d="M1.5 3.5 8 9l6.5-5.5"/></svg>
      dana@tarvikworks.com
    </p>
    <div class="contact__rule"></div>
    <p class="contact__motto">We will solve your EMC problems as early as possible—ideally before they even start</p>
  </div>

  <div class="front-mark"><span class="dot"></span><span>Tarvik Works, Inc.</span></div>
</section>

</body>
</html>
```